Embers Album Cover

3 panel design, 360mm x 120mm with title 'embers' (and sub-title mara coltby) on the right hand panel. Simple clean elegant design with a many stranded ribbon stretching right across the 3 panels, representing 'the river of life' (from the Bible). Plain, muted or textured background color.

```html
<!DOCTYPE html>
<html lang="en">
<head>
<meta charset="utf-8">
<title>Embers – mara coltby</title>
<link rel="stylesheet" href="https://fonts.googleapis.com/css2?family=Dancing+Script:wght@600;700&display=swap">
<style>
  :root {
    --deep-blue: #1b4776;
    --mid-blue: #3f7fb0;
    --pale-blue: #8fc0dc;
    --glow: #ffffff;
    --water: #5aa8d2;
    --strand: #ffffff;
    --ink-light: #ffffff;
  }
  html, body {
    margin: 0;
    padding: 0;
    overflow: hidden;
    background: #ffffff;
  }
  .cover {
    position: relative;
    width: 1200px;
    height: 400px;
    overflow: hidden;
    background: linear-gradient(90deg,
      var(--deep-blue) 0%,
      #245a8c 20%,
      var(--mid-blue) 34%,
      var(--pale-blue) 50%,
      var(--mid-blue) 68%,
      #2a6194 84%,
      var(--deep-blue) 100%);
  }
  .photo {
    position: absolute;
    left: 440px;
    top: 0;
    width: 380px;
    height: 400px;
    background:
      radial-gradient(ellipse 40% 75% at 48% 35%, var(--glow) 0%, rgba(255,255,255,0.9) 40%, rgba(255,255,255,0) 80%),
      linear-gradient(90deg, rgba(90,168,210,0) 0%, rgba(90,168,210,0.85) 10%, rgba(230,240,246,0.9) 28%, rgba(255,255,255,0.95) 50%, rgba(120,185,220,0.9) 72%, rgba(70,145,200,0.8) 88%, rgba(60,130,185,0) 100%);
  }
  .ribbon {
    position: absolute;
    inset: 0;
    width: 1200px;
    height: 400px;
  }
  .ribbon path { fill: var(--strand); }
  .title-block {
    position: absolute;
    left: 884px;
    top: 128px;
    color: var(--ink-light);
    font-family: "Dancing Script", cursive;
  }
  .title {
    margin: 0;
    font-size: 80px;
    font-weight: 700;
    line-height: 1;
  }
  .subtitle {
    margin: 2px 0 0 98px;
    font-size: 34px;
    font-weight: 600;
    line-height: 1;
  }
</style>
</head>
<body>
  <main class="cover">
    <div class="photo" role="img" aria-label="Photograph of a couple facing each other between two falling sheets of water, in pale blue and white tones"></div>
    <svg class="ribbon" viewBox="0 0 1200 400" aria-hidden="true">
      <path opacity="0.28" d="M-20 -30 C260 -30,420 150,610 150 C800 150,960 -40,1220 -40 C960 -34,800 160,610 160 C420 160,260 -4,-20 -4Z"/>
      <path opacity="0.32" d="M-20 40 C260 40,420 175,610 175 C800 175,960 20,1220 20 C960 26,800 185,610 185 C420 185,260 66,-20 66Z"/>
      <path opacity="0.24" d="M-20 110 C260 110,420 190,610 190 C800 190,960 70,1220 70 C960 76,800 200,610 200 C420 200,260 136,-20 136Z"/>
      <path opacity="0.3" d="M-20 180 C260 180,420 200,610 200 C800 200,960 300,1220 300 C960 306,800 210,610 210 C420 210,260 206,-20 206Z"/>
      <path opacity="0.26" d="M-20 250 C260 250,420 205,610 205 C800 205,960 330,1220 330 C960 336,800 215,610 215 C420 215,260 276,-20 276Z"/>
      <path opacity="0.32" d="M-20 320 C260 320,420 212,610 212 C800 212,960 360,1220 360 C960 366,800 222,610 222 C420 222,260 346,-20 346Z"/>
      <path opacity="0.26" d="M-20 390 C260 390,420 220,610 220 C800 220,960 390,1220 390 C960 396,800 230,610 230 C420 230,260 416,-20 416Z"/>
      <path opacity="0.3" d="M-20 440 C260 440,420 235,610 235 C800 235,960 420,1220 420 C960 426,800 245,610 245 C420 245,260 466,-20 466Z"/>
    </svg>
    <div class="title-block">
      <h1 class="title">Embers</h1>
      <p class="subtitle">mara coltby</p>
    </div>
  </main>
</body>
</html>
```